Supplement business needs a label design

We need a label design for our company VANTRELO LLC in The Woodlands, Texas,
This label is for a Fish Oil supplement.
Here is the task:
1. The text needs to be bold and readable on smartphone ads
2. The background is in a basic standard color like blue, silver, black, brown, etc
3. A watermark is on the background-color (waves, leaves, etc.).
4. The Brand will be "V A N T R E L O" with the attached logo design and "CU T T I N G E D G E F O R MU L A SU P P L E M E N T " :
5. Further details have to be on the label like on the attached Fish oil sample: "450 E P A / 300 D H A 1 , 2 5 0 M G DIETARY SUPPLEMENT GLUTENFREE with the icon and heart icon.
6. Please see attached samples:

```html
<!DOCTYPE html>
<html lang="en">
<head>
<meta charset="utf-8">
<title>VANTRELO Lifestyle Fish Oil Label</title>
<link rel="stylesheet" href="https://fonts.googleapis.com/css2?family=Montserrat:wght@600;700;800&family=Great+Vibes&display=swap">
<style>
  :root {
    --page-bg: #ececec;
    --label-black: #060606;
    --label-white: #ffffff;
    --band-red: #d8261c;
    --band-red-light: #e8503f;
    --art-ember: #7a2a14;
    --art-rust: #b4461e;
    --wave-line: rgba(255, 255, 255, 0.07);
  }
  * { box-sizing: border-box; margin: 0; padding: 0; }
  html, body {
    width: 1200px;
    height: 960px;
    overflow: hidden;
    background: var(--page-bg);
  }
  .canvas {
    position: relative;
    width: 1200px;
    height: 960px;
  }
  .label {
    position: absolute;
    left: 150px;
    top: 70px;
    width: 900px;
    height: 820px;
    background: var(--label-black);
    overflow: hidden;
    color: var(--label-white);
    font-family: "Montserrat", Arial, sans-serif;
  }
  .hero-art {
    position: absolute;
    left: 80px;
    top: 110px;
    width: 760px;
    height: 710px;
    background:
      radial-gradient(ellipse 45% 38% at 45% 40%, var(--art-rust) 0%, var(--art-ember) 45%, rgba(26,12,8,0) 100%),
      radial-gradient(ellipse 40% 35% at 55% 85%, var(--art-ember) 0%, rgba(26,12,8,0) 100%);
    opacity: 0.85;
  }
  .wave-watermark {
    position: absolute;
    left: 0;
    top: 0;
    width: 900px;
    height: 820px;
  }
  .brand {
    position: absolute;
    top: 48px;
    left: 0;
    width: 100%;
    display: flex;
    justify-content: center;
    align-items: center;
    gap: 18px;
  }
  .brand-mark {
    width: 22px;
    height: 22px;
    border-radius: 50%;
    background: var(--label-white);
  }
  .brand-name {
    font-weight: 700;
    font-size: 60px;
    letter-spacing: 1px;
    line-height: 1;
  }
  .line-name {
    position: absolute;
    top: 135px;
    width: 100%;
    text-align: center;
    font-family: "Great Vibes", cursive;
    font-size: 84px;
    line-height: 1;
  }
  .product-name {
    position: absolute;
    top: 235px;
    width: 100%;
    text-align: center;
    font-weight: 800;
    font-size: 190px;
    line-height: 1;
    letter-spacing: -2px;
    white-space: nowrap;
  }
  .ingredient-band {
    position: absolute;
    left: 0;
    top: 470px;
    width: 100%;
    height: 96px;
    background: linear-gradient(90deg, var(--band-red) 0%, var(--band-red) 60%, var(--band-red-light) 100%);
    transform: skewY(1.2deg);
    display: flex;
    align-items: center;
    justify-content: center;
  }
  .ingredient-band span {
    font-family: "Great Vibes", cursive;
    font-size: 56px;
    transform: skewY(-3deg);
    line-height: 1;
  }
  .dose {
    position: absolute;
    top: 588px;
    width: 100%;
    text-align: center;
    font-weight: 800;
    font-size: 38px;
    letter-spacing: 1px;
    line-height: 1;
    white-space: nowrap;
  }
  .tagline, .category {
    position: absolute;
    width: 100%;
    text-align: center;
    font-weight: 700;
    font-size: 34px;
    letter-spacing: 1px;
    line-height: 1;
    white-space: nowrap;
  }
  .tagline { top: 642px; }
  .category { top: 688px; }
  .icon-heart {
    position: absolute;
    left: 80px;
    top: 712px;
    width: 76px;
    height: 76px;
  }
  .badge-gluten {
    position: absolute;
    right: 60px;
    top: 712px;
    width: 130px;
    text-align: center;
  }
  .badge-gluten svg { width: 62px; height: 62px; }
  .badge-gluten span {
    display: block;
    margin-top: 4px;
    font-weight: 700;
    font-size: 15px;
  }
</style>
</head>
<body>
<div class="canvas">
  <div class="label">
    <div class="hero-art" role="img" aria-label="Photograph of a red betta fish with flowing fins on a dark background"></div>

    <svg class="wave-watermark" viewBox="0 0 900 820" fill="none" stroke="var(--wave-line)" stroke-width="3" aria-hidden="true">
      <path d="M0 130 Q75 100 150 130 T300 130 T450 130 T600 130 T750 130 T900 130"/>
      <path d="M0 170 Q75 140 150 170 T300 170 T450 170 T600 170 T750 170 T900 170"/>
      <path d="M0 410 Q75 380 150 410 T300 410 T450 410 T600 410 T750 410 T900 410"/>
      <path d="M0 450 Q75 420 150 450 T300 450 T450 450 T600 450 T750 450 T900 450"/>
      <path d="M0 760 Q75 730 150 760 T300 760 T450 760 T600 760 T750 760 T900 760"/>
      <path d="M0 800 Q75 770 150 800 T300 800 T450 800 T600 800 T750 800 T900 800"/>
    </svg>

    <div class="brand">
      <span class="brand-mark"></span>
      <span class="brand-name">VANTRELO</span>
    </div>

    <div class="line-name">Lifestyle</div>
    <div class="product-name">Fish Oil</div>

    <div class="ingredient-band"><span>With Organic Olive Oil</span></div>

    <div class="dose">450 EPA / 300 DHA &nbsp;1,250 MG</div>
    <div class="tagline">CUTTING EDGE FORMULA SUPPLEMENT</div>
    <div class="category">DIETARY SUPPLEMENT</div>

    <svg class="icon-heart" viewBox="0 0 76 76" fill="none" stroke="#ffffff" stroke-width="3.5" stroke-linecap="round" stroke-linejoin="round" aria-label="Heart health icon" role="img">
      <path d="M38 66 L12 38 C2 27 8 10 22 10 C30 10 35 15 38 20 C41 15 46 10 54 10 C66 10 72 24 66 34"/>
      <path d="M56 48 V68 M46 58 H66"/>
    </svg>

    <div class="badge-gluten">
      <svg viewBox="0 0 66 66" fill="none" stroke="#ffffff" stroke-width="2.5" stroke-linecap="round" aria-label="Gluten free icon" role="img">
        <circle cx="33" cy="33" r="30"/>
        <path d="M33 54 V16"/>
        <path d="M33 24 l-7 -5 M33 24 l7 -5 M33 33 l-7 -5 M33 33 l7 -5 M33 42 l-7 -5 M33 42 l7 -5"/>
        <path d="M12 54 L54 12"/>
      </svg>
      <span>GLUTENFREE</span>
    </div>
  </div>
</div>
</body>
</html>
```